Travel / Surf Shop Brochure

We are running a surf shop and also we are organising surf and multi-sport (bike, longboard, kaiak) trips in summer.
We need a concise well designed brochure to promote our trips (max 4 activities) and also our shop (maybe including few featured products).
We want to keep our production cost low, so a folded brochure would be good start for us.
As an idea you can review our Facebook profile (https://www.facebook.com/tidelark.store), see the photos, etc.
I can provide any photo from there in good resolution.
The surf destination is Portugal, so you can use any blow-mind pic of this destination.
When I'm first looking this brochure I have to think "I NEED IT, I WANT TO GO THERE". The look and feel should be around the the idea of well-being and outdoor entertainment.
The texts will NOT be in english so for the moment you can use some ample or english texts.
Updates
The logo is uploaded.
Please contact me for any requests or questions.
New pictures are uploaded.
Target Market(s)
We are talking with young and mature public, 25-35 years old, active pople.
Industry/Entity Type
Shop
Look and feel

```html
<!DOCTYPE html>
<html lang="en">
<head>
<meta charset="utf-8">
<title>Tidelark – Ski &amp; Surf Trips Brochure</title>
<link href="https://fonts.googleapis.com/css2?family=Oswald:wght@300;400;600&family=Permanent+Marker&family=Raleway:ital,wght@0,400;1,400&display=swap" rel="stylesheet">
<style>
  :root {
    --paper: #ffffff;
    --ink: #1a1a1a;
    --sun: #f2d000;
    --sky: #1e9ad6;
    --mark: #e8c400;
    --sky-grey: #cbc8c3;
    --sea-deep: #3f7d6d;
    --sea-green: #5e9a86;
    --foam: #e9ecea;
    --sand: #8b7b71;
    --sand-dark: #5e4e47;
    --map-grey: #a3a3a3;
    --map-light: #d6d6d6;
  }
  * { margin: 0; padding: 0; box-sizing: border-box; }
  html, body { width: 1200px; height: 850px; overflow: hidden; background: var(--paper); }
  .brochure {
    position: absolute; left: 12px; top: 10px; width: 1176px; height: 830px;
    display: flex; box-shadow: 0 2px 8px rgba(0,0,0,.35);
  }
  .panel { position: relative; height: 100%; overflow: hidden; }
  .panel--trip { width: 384px; }
  .panel--world { width: 404px; background: var(--paper); }
  .panel--cover { width: 388px; }

  .photo { position: absolute; inset: 0; }
  .photo--trip {
    background: linear-gradient(180deg, var(--sky-grey) 0%, #c3c2bd 30%, #8fb0a5 34%, var(--sea-deep) 42%, var(--foam) 52%, var(--sea-green) 60%, #a9bfb6 68%, var(--sand) 76%, var(--sand-dark) 88%, var(--sand) 100%);
  }
  .photo--cover {
    background: linear-gradient(180deg, #d0cdc9 0%, #c8c6c1 32%, #8aaea1 36%, var(--foam) 46%, var(--sea-green) 54%, var(--sea-deep) 64%, #7fb1a1 70%, var(--foam) 74%, var(--sand) 80%, var(--sand-dark) 90%, var(--sand) 100%);
  }

  .trip-title {
    position: absolute; font-family: "Oswald", sans-serif; font-weight: 300;
    color: var(--ink); line-height: 1;
  }
  .trip-title--top { right: 346px; top: 62px; font-size: 96px; }
  .trip-title--bottom { left: -4px; top: 526px; font-size: 100px; letter-spacing: 2px; }
  .destination {
    position: absolute; left: 76px; top: 116px;
    font-family: "Oswald", sans-serif; font-weight: 300; font-size: 17px; color: var(--ink);
  }
  .destination__country { color: var(--sun); }
  .trip-note {
    position: absolute; left: 144px; top: 152px;
    font-family: "Raleway", sans-serif; font-size: 9px; line-height: 1.5; color: var(--ink);
  }
  .trip-note__link { font-style: italic; }
  .orbit { position: absolute; inset: 0; }

  .world-map {
    position: absolute; left: 48px; top: 280px; width: 354px; height: 196px;
    background:
      radial-gradient(ellipse 38% 46% at 36% 58%, rgba(140,140,140,.55), rgba(140,140,140,0) 100%),
      radial-gradient(ellipse 55% 50% at 50% 45%, var(--map-light) 0%, rgba(214,214,214,.6) 60%, rgba(214,214,214,0) 100%);
  }
  .headline {
    position: absolute; left: 102px; top: 606px;
    font-family: "Oswald", sans-serif; font-size: 20px; line-height: 1.2; color: var(--ink);
  }
  .headline__lead { color: var(--sky); font-weight: 300; }
  .headline__line { font-weight: 400; }
  .contact {
    position: absolute; left: 174px; top: 698px;
    font-family: "Raleway", sans-serif; font-style: italic; font-size: 9px; line-height: 1.35; color: var(--ink);
  }

  .brand { position: absolute; left: 156px; top: 38px; text-align: center; }
  .brand__row { display: flex; align-items: center; gap: 4px; }
  .brand__dot { width: 12px; height: 12px; background: var(--mark); }
  .brand__name {
    font-family: "Oswald", sans-serif; font-weight: 600; font-size: 20px; line-height: 1; color: var(--sky);
  }
  .brand__tag {
    margin-top: 5px; font-family: "Oswald", sans-serif; font-weight: 400; font-size: 6px; letter-spacing: .5px; color: var(--ink);
  }
  .cover-title {
    position: absolute; inset: 0;
    font-family: "Permanent Marker", cursive; font-weight: 400; font-size: 84px;
    line-height: 1; color: var(--ink);
  }
  .cover-title__line { position: absolute; white-space: nowrap; }
  .cover-title__line--ski { left: 64px; top: 84px; }
  .cover-title__line--surf { left: 40px; top: 172px; }
  .cover-title__line--shop { left: 94px; top: 262px; }
</style>
</head>
<body>
  <main class="brochure">
    <section class="panel panel--trip">
      <div class="photo photo--trip" role="img" aria-label="Photo of a surfer riding a breaking green wave off the coast of Portugal, sandy beach blurred in the foreground"></div>
      <svg class="orbit" width="384" height="830" viewBox="0 0 384 830" aria-hidden="true">
        <circle cx="-24" cy="314" r="132" fill="none" stroke="#1a1a1a" stroke-width="2" stroke-dasharray="2 4"/>
      </svg>
      <p class="trip-title trip-title--top">TRIPS</p>
      <p class="destination"><span class="destination__country">PORTUGAL</span> &gt; SURF DESTINATION</p>
      <p class="trip-note">check for more trip activities at<br><span class="trip-note__link">www.tidelarktrips.com</span></p>
      <p class="trip-title trip-title--bottom">A TRIP.</p>
    </section>

    <section class="panel panel--world">
      <div class="world-map" role="img" aria-label="Grey world map with trip destinations highlighted in light blue and magenta"></div>
      <svg class="orbit" width="404" height="830" viewBox="0 0 404 830" aria-hidden="true">
        <path d="M0 224 A 236 236 0 0 1 342 178" fill="none" stroke="#1a1a1a" stroke-width="1.5"/>
        <polyline points="331,169 342,178 329,182" fill="none" stroke="#1a1a1a" stroke-width="1.5"/>
        <path d="M402 434 A 236 236 0 0 1 222 564" fill="none" stroke="#1a1a1a" stroke-width="1.5"/>
        <polyline points="233,556 222,564 233,572" fill="none" stroke="#1a1a1a" stroke-width="1.5"/>
        <circle cx="198" cy="374" r="120" fill="none" stroke="#1a1a1a" stroke-width="3"/>
        <circle cx="208" cy="368" r="84" fill="none" stroke="#1a1a1a" stroke-width="2" stroke-dasharray="2 4"/>
      </svg>
      <div class="headline">
        <p class="headline__lead">ALL OVER THE WORLD</p>
        <p class="headline__line">&gt; TRIPS DESTINATIONS,</p>
        <p class="headline__line">ADVENTURE AND FUN.</p>
      </div>
      <p class="contact">Tidelark ski and surf<br>+ 351 214 560<br>www.tidelark.store</p>
    </section>

    <section class="panel panel--cover">
      <div class="photo photo--cover" role="img" aria-label="Photo of a large green wave breaking toward a blurred sandy shore"></div>
      <div class="brand">
        <div class="brand__row"><span class="brand__dot"></span><span class="brand__name">TIDELARK</span></div>
        <p class="brand__tag">SKI &amp; SURF SHOP</p>
      </div>
      <h1 class="cover-title">
        <span class="cover-title__line cover-title__line--ski">SKI &amp;</span>
        <span class="cover-title__line cover-title__line--surf">SURF</span>
        <span class="cover-title__line cover-title__line--shop">SHOP</span>
      </h1>
    </section>
  </main>
</body>
</html>
```